Stationary Design For Youthful Disability Company

Hi Designers,
Looking to have our brand applied to a range of stationary items to professionalise our approach, we are a disability services company that aligns young carers with disabled youth and adults. Our stationary needs to look professional but can verge into a fun bright territory too.
Winning designer will be first contact for advertising campaign, form creation and web-design in January 2014.
Cheers,
Tom
Brightpath Disability Services
Design Briefs
Stationary.
Sleek fun and bright stationary that portrays a professional but youthful disability service. Company prides its self on delivering youthful carers to disabled clients.
Needed:
- Business Card - Letter Head - Email Signature
- Invoice / Quotation (blank branded paper) - Normal Envelope - A4 Envelope
- Stationary for future forms or documents. (Doesn't need to include all contacts, branding is enough).
Would be nice if we were able to edit numbers etc as we change them.
Include:
Thomas Wexford - Managing Director
M. 0458 927 304
E. twexford@brightpathcare.example
A. PO Box 78 Larchmere 3190
ABN. 47392051864

```html
<!DOCTYPE html>
<html lang="en">
<head>
<meta charset="utf-8">
<title>Brightpath Disability Services – Business Card</title>
<link rel="stylesheet" href="https://fonts.googleapis.com/css2?family=Open+Sans:ital,wght@0,400;0,700;1,700&display=swap">
<style>
  :root {
    --page-bg: #e9e6e4;
    --card-dark: #1d1c1c;
    --card-light: #ffffff;
    --ink: #3a3a3c;
    --ink-soft: #4a4a4c;
    --brand-blue: #1b8fcf;
    --brand-light: #eaeaea;
    --blob-lilac: #cbbcd8;
    --blob-blue: #a9cdd9;
    --blob-peach: #eccaa8;
    --blob-green: #d8e6c0;
    --blob-pink: #e3c3cf;
  }
  * { box-sizing: border-box; margin: 0; padding: 0; }
  html, body { width: 1200px; height: 900px; overflow: hidden; }
  body {
    background: var(--page-bg);
    font-family: "Open Sans", Arial, sans-serif;
    display: flex;
    flex-direction: column;
    align-items: center;
    justify-content: center;
    gap: 50px;
  }
  .card {
    width: 665px;
    height: 380px;
    position: relative;
    overflow: hidden;
    box-shadow: 0 6px 18px rgba(0,0,0,.18);
  }

  /* Back of card */
  .card--back {
    background: var(--card-dark);
    display: flex;
    align-items: center;
    justify-content: center;
  }
  .brand-lockup--back {
    display: flex;
    align-items: center;
    gap: 16px;
  }
  .brand-dot {
    width: 30px; height: 30px;
    border-radius: 50%;
    background: var(--brand-blue);
    flex: none;
  }
  .brand-name--back {
    color: var(--brand-light);
    font-weight: 700;
    font-size: 26px;
    letter-spacing: .04em;
    line-height: 1.15;
    text-transform: uppercase;
  }

  /* Front of card */
  .card--front { background: var(--card-light); }
  .card-art {
    position: absolute;
    right: 0; top: 0;
    width: 52%;
    height: 100%;
  }
  .brand-lockup--front {
    position: absolute;
    left: 52px; top: 88px;
    display: flex;
    align-items: center;
    gap: 12px;
  }
  .brand-lockup--front .brand-dot { width: 22px; height: 22px; }
  .brand-name--front {
    color: var(--brand-blue);
    font-weight: 700;
    font-size: 17px;
    line-height: 1.1;
    letter-spacing: .03em;
    text-transform: uppercase;
  }
  .person {
    position: absolute;
    left: 52px; top: 170px;
    color: var(--ink);
  }
  .person-name { font-size: 22px; font-weight: 700; }
  .person-role { font-size: 15px; font-weight: 700; font-style: italic; margin-top: 1px; }
  .contact-list {
    position: absolute;
    left: 52px; top: 264px;
    list-style: none;
    font-size: 12px;
    color: var(--ink-soft);
    line-height: 20px;
  }
  .contact-list li { display: flex; align-items: center; gap: 8px; }
  .contact-label { font-weight: 700; }
  .contact-icon { width: 16px; height: 16px; flex: none; fill: var(--ink); }
  .contact-at { width: 16px; text-align: center; font-weight: 700; font-size: 15px; color: var(--ink); }
</style>
</head>
<body>

  <section class="card card--back" aria-label="Business card, reverse side">
    <div class="brand-lockup brand-lockup--back">
      <span class="brand-dot"></span>
      <p class="brand-name brand-name--back">Brightpath<br>Disability Services</p>
    </div>
  </section>

  <section class="card card--front" aria-label="Business card, front side">
    <svg class="card-art" viewBox="0 0 346 380" role="img" aria-label="Soft pastel flowing shapes in lilac, blue, peach and green" preserveAspectRatio="none">
      <defs>
        <linearGradient id="pastelWash" x1="0" y1="0" x2="1" y2="1">
          <stop offset="0" stop-color="var(--blob-green)" stop-opacity="0"/>
          <stop offset=".35" stop-color="var(--blob-lilac)" stop-opacity=".75"/>
          <stop offset=".6" stop-color="var(--blob-blue)" stop-opacity=".8"/>
          <stop offset=".85" stop-color="var(--blob-peach)" stop-opacity=".8"/>
          <stop offset="1" stop-color="var(--blob-pink)" stop-opacity=".8"/>
        </linearGradient>
      </defs>
      <rect width="346" height="380" fill="url(#pastelWash)"/>
    </svg>

    <div class="brand-lockup brand-lockup--front">
      <span class="brand-dot"></span>
      <p class="brand-name brand-name--front">Brightpath<br>Disability Services</p>
    </div>

    <div class="person">
      <h1 class="person-name">Thomas Wexford</h1>
      <p class="person-role">Managing Director</p>
    </div>

    <ul class="contact-list">
      <li><span><span class="contact-label">ABN#</span> 47392051864</span></li>
      <li>
        <svg class="contact-icon" viewBox="0 0 16 16" aria-hidden="true"><path d="M8 1 0.5 8h2.5v7h4v-4h2v4h4V8h2.5z"/></svg>
        <span>A. PO Box 78 Larchmere 3190</span>
      </li>
      <li>
        <svg class="contact-icon" viewBox="0 0 16 16" aria-hidden="true"><path d="M1 5c0-2 3-3 7-3s7 1 7 3v1.5h-3.5V5h-7v1.5H1zM3 8h10l1.5 6h-13zm5 1.5a2 2 0 1 0 0 4 2 2 0 0 0 0-4z"/></svg>
        <span>+ 0458 927 304</span>
      </li>
      <li>
        <span class="contact-at">@</span>
        <span>E. twexford@brightpathcare.example</span>
      </li>
    </ul>
  </section>

</body>
</html>
```